Halvorsen Electric service department flyer

Looking to design a electrical service department flyer. The company has been in San Francisco for 60yrs primarily doing work in the downtown area. https://halvorsenelectric.example/about-halvorsen/
I attached a rough draft of the flyer. I would like to see something with the san francisco downtown skyline watermarked on the front page, open to the second page that describes all services and contact.

```html
<!DOCTYPE html>
<html lang="en">
<head>
<meta charset="utf-8">
<title>Halvorsen Electric – Electrical / Datacom Flyer</title>
<link rel="stylesheet" href="https://fonts.googleapis.com/css2?family=Anton&family=Poppins:wght@400;600;700&display=swap">
<style>
  :root {
    --navy: #0050a5;
    --sky: #16abe0;
    --ink: #333338;
    --heading-ink: #3a3a40;
    --rule: #8a8a8a;
    --page-bg: #ececec;
    --white: #ffffff;
  }
  * { box-sizing: border-box; margin: 0; padding: 0; }
  html, body { width: 974px; height: 1200px; overflow: hidden; }
  body {
    background: var(--page-bg);
    font-family: "Poppins", sans-serif;
    color: var(--ink);
    position: relative;
  }
  .flyer {
    position: absolute;
    left: 77px; top: 20px;
    width: 819px; height: 1159px;
    background: var(--white);
    overflow: hidden;
  }
  .skyline-photo {
    position: absolute; left: 0; top: 0;
    width: 819px; height: 480px;
    background: linear-gradient(180deg,
      #38373c 0%, #3c3b46 14%, #4a4560 30%, #6a5878 42%,
      #c46a6a 52%, #f08a4a 58%, #f6b45a 62%, #8a6a70 68%,
      #4a4050 76%, #2e2a32 88%, #24222a 100%);
  }
  .brand-name {
    position: absolute; left: 90px; top: 145px;
    font-family: "Poppins", sans-serif;
    font-weight: 700; font-size: 34px;
    color: var(--white); letter-spacing: 0.5px;
  }
  .bands { position: absolute; left: 0; top: 0; width: 819px; height: 1159px; }
  .headline {
    position: absolute; left: 0; top: 495px; width: 819px;
    text-align: center;
    font-family: "Anton", sans-serif;
    font-size: 64px; line-height: 117px; letter-spacing: 0.5px;
    color: var(--white);
  }
  .intro {
    position: absolute; left: 77px; top: 665px; width: 680px;
    font-size: 15.6px; line-height: 23.3px; color: var(--ink);
  }
  .intro strong { font-weight: 700; }
  .section-pill {
    position: absolute; left: 77px; top: 764px;
    width: 243px; height: 41px;
    background: var(--sky); border-radius: 21px;
  }
  .section-pill span {
    position: absolute; left: 29px; top: 0;
    width: 214px; height: 41px;
    background: var(--navy); border-radius: 21px;
    box-shadow: -3px 0 0 var(--white);
    color: var(--white); font-weight: 700; font-size: 22px;
    line-height: 42px; text-align: center;
  }
  .service-group { position: absolute; left: 99px; width: 640px; }
  .service-group.residential { top: 822px; }
  .service-group.commercial { top: 948px; }
  .group-title {
    display: flex; align-items: center; gap: 16px;
    font-weight: 700; font-size: 18px; color: var(--heading-ink);
    text-transform: uppercase; height: 24px;
  }
  .group-title::after {
    content: ""; flex: 1; height: 1px; background: var(--rule);
  }
  .service-columns { display: flex; margin-top: 11px; }
  .service-list {
    list-style: none; position: relative;
    padding-left: 14px; font-size: 15.2px; line-height: 22.7px;
    color: var(--ink);
  }
  .service-list.left { width: 399px; }
  .service-list::before {
    content: ""; position: absolute; left: 2.5px;
    top: 8px; bottom: 8px; width: 1.5px; background: var(--navy);
  }
  .service-list li { position: relative; }
  .service-list li::before {
    content: ""; position: absolute; left: -14px; top: 9px;
    width: 5px; height: 5px; border-radius: 50%; background: var(--navy);
  }
  .site-url {
    position: absolute; left: 0; top: 1091px; width: 819px;
    text-align: center; font-size: 17px; letter-spacing: 5.2px;
    color: var(--white);
  }
</style>
</head>
<body>
  <main class="flyer">
    <div class="skyline-photo" role="img" aria-label="Photo of the San Francisco downtown skyline and Bay Bridge at sunset"></div>
    <div class="brand-name">Halvorsen Electric</div>

    <svg class="bands" viewBox="0 0 1092 1545" aria-hidden="true">
      <polygon points="0,630 700,643 0,660" fill="var(--navy)"/>
      <polygon points="0,660 1092,622 1092,660" fill="var(--sky)"/>
      <rect x="0" y="659" width="1092" height="158" fill="var(--navy)"/>
      <polygon points="0,816 1092,816 0,856" fill="var(--sky)"/>
      <polygon points="1092,816 1092,856 540,836" fill="var(--navy)"/>
      <rect x="0" y="1436" width="1092" height="109" fill="var(--navy)"/>
      <rect x="0" y="1512" width="1092" height="5" fill="var(--white)"/>
      <rect x="102" y="1512" width="888" height="6" fill="var(--sky)"/>
    </svg>

    <h1 class="headline">ELECTRICAL / DATACOM</h1>

    <p class="intro"><strong>Halvorsen</strong> Electric is a licensed electrical contractor proudly serving San Francisco and surrounding Bay Area communities. Our experienced electricians provide safe, efficient, and code-compliant electrical solutions for residential and commercial properties.</p>

    <div class="section-pill"><span>Our Services</span></div>

    <section class="service-group residential">
      <h2 class="group-title">Residential Electrical</h2>
      <div class="service-columns">
        <ul class="service-list left">
          <li>Electrical repairs &amp; troubleshooting</li>
          <li>Panel upgrades &amp; breaker replacement</li>
          <li>Lighting installation (indoor &amp; outdoor)</li>
        </ul>
        <ul class="service-list">
          <li>EV charger installation</li>
          <li>Rewiring &amp; remodels</li>
          <li>Emergency electrical services</li>
        </ul>
      </div>
    </section>

    <section class="service-group commercial">
      <h2 class="group-title">Commercial Electrical</h2>
      <div class="service-columns">
        <ul class="service-list left">
          <li>Office &amp; retail electrical systems</li>
          <li>Lighting upgrades &amp; maintenance</li>
          <li>Electrical inspections</li>
        </ul>
        <ul class="service-list">
          <li>Tenant improvements</li>
          <li>Emergency electrical services</li>
        </ul>
      </div>
    </section>

    <p class="site-url">www.halvorsenelectric.example</p>
  </main>
</body>
</html>
```